Facebook post for announcing the new company's website design

Need a facebook post (English language) for announcing that the company has a renovated website:
https://www.sanavistaclinica.com/en/

The website existed already but received recently a brand new design: more light, modern and sophisticated.

Please find as an attachment source files of our logo so that you can provide the best quality, thanks.

Also you may find our facebook page at:
https://pt-pt.facebook.com/sanavistaclinica/

Target Market(s)

Facebook audience

Colors

Designer to choose colors to be used in the design.

Requirements
Must have
• Our website has a new design!
• www.sanavistaclinica.com
Nice to have
• The post should feel as somehow connected to the website. Please check our above mentioned website, things should be related. For instance, use our logo (check attached files).
• You may also use this opportunity to remind the audience about our business core messages: excellency, quality, safety.

```html
<!DOCTYPE html>
<html lang="en">
<head>
<meta charset="utf-8">
<title>Sanavista Clínica – Facebook cover</title>
<link href="https://fonts.googleapis.com/css2?family=Montserrat:wght@400;500;600;700&display=swap" rel="stylesheet">
<style>
  :root {
    --page-bg: #f7f7f7;
    --cover-deep: #4f93b8;
    --cover-mid: #5aa7c9;
    --cover-light: #62b5d6;
    --band: #5fc0dc;
    --white: #ffffff;
    --brand-blue: #1b7ca8;
    --brand-grey: #6d7f8a;
  }
  html, body {
    margin: 0;
    padding: 0;
    width: 1200px;
    height: 904px;
    overflow: hidden;
    background: var(--page-bg);
  }
  .canvas {
    width: 1200px;
    height: 904px;
    display: flex;
    align-items: center;
    justify-content: center;
  }
  .cover {
    width: 1120px;
    height: 426px;
    display: block;
    box-shadow: 0 24px 40px -22px rgba(0, 0, 0, 0.28);
  }
  .value-label {
    font-family: "Montserrat", sans-serif;
    font-weight: 600;
    font-size: 19px;
    letter-spacing: 0.6px;
    fill: var(--white);
  }
  .headline {
    font-family: "Montserrat", sans-serif;
    font-weight: 600;
    font-size: 16px;
    letter-spacing: 0.4px;
    fill: var(--white);
  }
  .site-url {
    font-family: "Montserrat", sans-serif;
    font-weight: 500;
    font-size: 12.5px;
    letter-spacing: 2.4px;
    fill: var(--white);
  }
  .brand-name {
    font-family: "Montserrat", sans-serif;
    font-weight: 700;
    font-size: 20px;
    fill: var(--brand-blue);
  }
  .brand-sub {
    font-family: "Montserrat", sans-serif;
    font-weight: 400;
    font-size: 7.5px;
    fill: var(--brand-grey);
  }
</style>
</head>
<body>
<main class="canvas">
  <svg class="cover" viewBox="0 0 820 312" xmlns="http://www.w3.org/2000/svg">
    <defs>
      <linearGradient id="coverTone" x1="0" y1="0" x2="1" y2="0">
        <stop offset="0" stop-color="var(--cover-deep)"/>
        <stop offset="0.5" stop-color="var(--cover-mid)"/>
        <stop offset="1" stop-color="var(--cover-light)"/>
      </linearGradient>
      <radialGradient id="portraitTone" cx="0.5" cy="0.4" r="0.6">
        <stop offset="0" stop-color="#7fb6cf"/>
        <stop offset="1" stop-color="#5aa7c9" stop-opacity="0"/>
      </radialGradient>
    </defs>

    <rect class="cover-background" width="820" height="312" fill="url(#coverTone)"/>
    <rect class="portrait-area" x="400" y="0" width="420" height="312" fill="url(#portraitTone)"
          role="img" aria-label="Photo of a smiling senior doctor in a white coat, tinted blue"/>

    <rect class="url-band" x="0" y="252" width="820" height="60" fill="var(--band)" opacity="0.55"/>

    <g class="values" stroke="var(--white)" fill="none" stroke-width="1.4">
      <line x1="142" y1="0" x2="142" y2="38.5"/>
      <line x1="142" y1="81.5" x2="142" y2="105.5"/>
      <line x1="142" y1="148.5" x2="142" y2="173.5"/>
      <circle cx="142" cy="60" r="21.5"/>
      <circle cx="142" cy="127" r="21.5"/>
      <circle cx="142" cy="195" r="21.5"/>
      <path d="M133 60 l6 6 l11 -12" stroke-width="1.8"/>
      <path d="M133 127 l6 6 l11 -12" stroke-width="1.8"/>
      <path d="M133 195 l6 6 l11 -12" stroke-width="1.8"/>
    </g>
    <text class="value-label" x="194" y="67">EXCELLENCY</text>
    <text class="value-label" x="194" y="134">QUALITY</text>
    <text class="value-label" x="194" y="202">SAFETY</text>

    <text class="headline" x="120" y="276">Our website has a new design!</text>
    <text class="site-url" x="120" y="297">www.sanavistaclinica.com</text>

    <g class="brand-badge">
      <rect x="503" y="192" width="239" height="81" rx="40.5" fill="var(--white)"/>
      <circle cx="553" cy="232.5" r="16" fill="var(--brand-blue)"/>
      <text class="brand-name" x="577" y="231">Sanavista</text>
      <text class="brand-name" x="577" y="251">Clínica</text>
      <text class="brand-sub" x="577" y="262">Professor Doutor Rui Almada</text>
    </g>
  </svg>
</main>
</body>
</html>
```